Company or website name
- www.brelmontpath.com
- Links to the website
- Owner of Brelmontpath. We serve real estate brokers, managers & sales associates with consulting, coaching and training solutions. My site is being redesigned to be more focused on target audience.
- Other Facts

```html
<!DOCTYPE html>
<html lang="en">
<head>
<meta charset="utf-8">
<title>Ten Traits for Top Performers – Brelmontpath</title>
<link rel="stylesheet" href="https://fonts.googleapis.com/css2?family=Cinzel:wght@400;700&family=PT+Sans&display=swap">
<style>
  :root {
    --backdrop: #aeab8c;
    --panel-dark: #343434;
    --map-grey: #9a9a9a;
    --frame-black: #000000;
    --white: #ffffff;
    --ink: #2b2b2b;
    --link-blue: #1d7fb8;
    --accent-orange: #f07a1c;
    --accent-blue: #1c8ad6;
  }
  * { margin: 0; padding: 0; box-sizing: border-box; }
  html, body { width: 1200px; height: 924px; overflow: hidden; }
  body { background: var(--backdrop); position: relative; font-family: "PT Sans", sans-serif; }

  .back-cover {
    position: absolute; left: 51px; top: 73px; width: 549px; height: 778px;
    background: var(--panel-dark);
  }
  .back-cover .world-area {
    position: absolute; left: 117px; top: 328px; width: 302px; height: 151px;
    background: radial-gradient(ellipse at 50% 45%, rgba(154,154,154,0.75) 0%, rgba(154,154,154,0.45) 55%, rgba(154,154,154,0) 75%);
  }
  .testimonial-photo {
    position: absolute; left: 17px; top: 611px; width: 163px; height: 153px;
    border: 6px solid var(--frame-black);
    background: linear-gradient(180deg, #9cc3e0 0%, #a9b8c4 30%, #b08a72 55%, #3e6a48 80%, #2c5236 100%);
  }
  .testimonial-quote {
    position: absolute; left: 187px; top: 611px; width: 360px;
    color: var(--white); font-size: 22px; line-height: 29px;
  }
  .testimonial-author {
    position: absolute; left: 392px; top: 713px;
    color: var(--white); font-size: 22px; line-height: 32px;
  }

  .front-cover {
    position: absolute; left: 600px; top: 73px; width: 554px; height: 778px;
    background: var(--white); overflow: hidden;
  }
  .front-cover svg { position: absolute; left: 0; top: 0; }
  .cover-title {
    position: absolute; left: 174px; top: 10px; width: 380px;
    font-family: "Cinzel", serif; font-weight: 400; color: var(--white);
    font-size: 41px; line-height: 49px; letter-spacing: 0.5px;
    text-shadow: 1px 1px 2px rgba(0,0,0,0.35);
  }
  .cover-subtitle {
    position: absolute; left: 0; top: 680px; width: 554px; text-align: center;
    font-family: "Cinzel", serif; font-weight: 700; color: var(--ink);
    font-size: 28px; line-height: 35px;
  }
  .cover-link {
    position: absolute; left: 0; top: 739px; width: 554px; text-align: center;
    color: var(--link-blue); font-size: 25px; line-height: 30px; text-decoration: none; display: block;
  }
</style>
</head>
<body>

<section class="back-cover">
  <div class="world-area" role="img" aria-label="Grey world map silhouette"></div>
  <div class="testimonial-photo" role="img" aria-label="Portrait photo of the client giving the testimonial"></div>
  <p class="testimonial-quote">"This has helped my business.<br>&nbsp;There is nothing comparable for<br>&nbsp;a real estate broker.&nbsp; Thanks!"</p>
  <p class="testimonial-author">Dave R.<br>Jackson, MS</p>
</section>

<section class="front-cover">
  <svg width="554" height="778" viewBox="0 0 554 778">
    <defs>
      <linearGradient id="bannerFill" x1="0" y1="0" x2="1" y2="1">
        <stop offset="0" stop-color="#4fb0ea"/>
        <stop offset="0.35" stop-color="#1d78c8"/>
        <stop offset="1" stop-color="#0a3f86"/>
      </linearGradient>
      <linearGradient id="photoFill" x1="0" y1="0" x2="1" y2="1">
        <stop offset="0" stop-color="#8fae72"/>
        <stop offset="0.25" stop-color="#a4a089"/>
        <stop offset="0.45" stop-color="#c29c84"/>
        <stop offset="0.62" stop-color="#3b3842"/>
        <stop offset="0.85" stop-color="#2a2932"/>
        <stop offset="1" stop-color="#8a7466"/>
      </linearGradient>
      <linearGradient id="yellowWave" x1="0" y1="0" x2="1" y2="0">
        <stop offset="0" stop-color="#ffe02a"/>
        <stop offset="1" stop-color="#f6a914"/>
      </linearGradient>
    </defs>

    <rect class="cover-photo" x="0" y="110" width="554" height="560" fill="url(#photoFill)"
          role="img" aria-label="Photo of a real estate agent in a suit advising a client across a desk"/>

    <path class="banner" d="M0 0 H554 V122 C470 150 360 168 250 160 C160 152 70 120 0 118 Z" fill="url(#bannerFill)"/>
    <path class="banner-stripe" d="M0 118 C70 120 160 152 250 160 C360 168 470 150 554 122 V132 C470 162 360 178 250 170 C160 163 70 132 0 130 Z" fill="var(--white)"/>
    <path class="banner-stripe-orange" d="M0 130 C70 132 160 163 250 170 C360 178 470 162 554 132 V138 C470 170 360 186 250 178 C160 171 70 140 0 137 Z" fill="var(--accent-orange)"/>
    <rect class="banner-world" x="24" y="16" width="144" height="70" rx="20" fill="var(--white)" opacity="0.55"
          role="img" aria-label="White world map emblem"/>

    <path class="wave-yellow" d="M0 500 C120 540 260 560 400 550 C470 545 520 525 554 505 V560 C470 600 300 615 150 600 C90 594 40 585 0 575 Z" fill="url(#yellowWave)"/>
    <path class="wave-orange" d="M0 575 C40 585 90 594 150 600 C300 615 470 600 554 560 V585 C470 625 300 640 150 628 C90 622 40 612 0 603 Z" fill="var(--accent-orange)"/>
    <path class="wave-blue" d="M0 603 C40 612 90 622 150 628 C300 640 470 625 554 585 V605 C470 645 300 660 150 648 C90 642 40 632 0 622 Z" fill="var(--accent-blue)"/>
    <path class="cover-base" d="M0 622 C40 632 90 642 150 648 C300 660 470 645 554 605 V778 H0 Z" fill="var(--white)"/>
  </svg>

  <h1 class="cover-title">Ten Traits for<br>Top Performers</h1>
  <p class="cover-subtitle">A Real Estate Professional's<br>Guide to a Winning Career</p>
  <a class="cover-link" href="http://www.brelmontpath.com">www.brelmontpath.com</a>
</section>

</body>
</html>
```